Thistle Cafe's Web Page
Thank you for all the hardwork. Happy to see there are so many beautiful artworks. We have tried very hard to select the final winner. All the best in the year of Rabbit!!
We will post more contest later.Just stay tune!!
Good luck for all!!
good luck tremiko !!!
kindly rate template
thank you.
Can you kindly Rate our templates.
so that we will able to guess our work judgment.. how much effort we need more to create exact design!!!
Hi Guys! The reason I justified the work of Quillaro work is the outline of the web page not the software itself. When I look at the designs and the tones are mostly in black color and I think you will do the same thing as me. Do you all agree??
Corvel! your artwork is quite interesting too! Especially the slogan you made!! Your design is one of our consideration too!!
well i am waiting for your feedback. thanks
this whole thing is turning to a joke. enjoy
@ SirPlonk, Are you serious? You are only seeing part of my design. Please do not judge. Your comment is very offensive and you are belittling my work.
you're not serious are you ?
I think the design made by Quillarowork is quite attractive.
pomlet42 > Please let us know which designs you like so far. regards
Please check the design and rate :)
Best wishes
Wow! Quillarowork's design is quite nice. What's in the photo? Looks good!!
I found a website is quite interesting - http://www.brasvelo.com.au/. The designs that I recieved are similar. I hope the black color is not the only choice for us. Keep it going! Guys.Overall, the layouts are OK.
Just to verify, you will have both a set menu and a daily specials menu, is that correct. What other pages where you looking for on your site?
We are still renovating. It will be a good idea to spare some space for our cafe and our menu and special. We will be listen to any good suggestion!!
Logo has been uploaded
Thanks a lot :) I'M IN :)
Hi PH, Can you upload your logo so we know where to start? Thanks
We have a logo designed. It may be helpful to get some ideas. Please ask for it or browse the past projects (around late December) if needed.

```html
<!DOCTYPE html>
<html lang="en">
<head>
<meta charset="utf-8">
<title>Thistle Cafe</title>
<link rel="stylesheet" href="https://fonts.googleapis.com/css2?family=Arimo:wght@400;700&display=swap">
<style>
  :root {
    --page-white: #ffffff;
    --teal: #4b9cbb;
    --nav-teal: #3b8db0;
    --sidebar-dark: #1a2730;
    --footer-black: #0b0b0b;
    --text-white: #ffffff;
    --accent-orange: #f29a1f;
    --brand-dark: #2a2a2a;
  }
  * { margin: 0; padding: 0; box-sizing: border-box; }
  html, body { width: 1200px; height: 1009px; overflow: hidden; background: var(--page-white); }
  body { font-family: "Arimo", Arial, sans-serif; position: relative; }

  .site-header { position: absolute; left: 0; top: 0; width: 1200px; height: 286px; background: var(--page-white); }
  .sub-brand { position: absolute; left: 22px; top: 100px; display: flex; align-items: center; gap: 12px; }
  .sub-brand-mark { width: 22px; height: 22px; background: var(--accent-orange); }
  .sub-brand-name { color: var(--accent-orange); font-size: 40px; font-weight: 700; line-height: 48px; }
  .brand { position: absolute; left: 430px; top: 100px; display: flex; align-items: center; gap: 16px; }
  .brand-mark { width: 24px; height: 24px; border-radius: 50%; background: var(--brand-dark); }
  .brand-name { color: var(--brand-dark); font-size: 46px; font-weight: 400; line-height: 54px; }

  .main-nav { position: absolute; right: 28px; top: 246px; display: flex; gap: 52px; }
  .main-nav a { color: var(--nav-teal); text-decoration: none; font-size: 29px; }

  .content-band { position: absolute; left: 0; top: 286px; width: 1200px; height: 677px; background: var(--teal); }

  .meal-sidebar { position: absolute; left: 27px; top: 0; width: 274px; height: 677px; background: var(--sidebar-dark); }
  .meal { position: absolute; left: 11px; width: 259px; }
  .meal-photo { display: block; width: 259px; height: 162px; background: linear-gradient(135deg, #c89a5a, #f3ede0 55%, #8fae5a); }
  .meal-label { color: var(--text-white); font-size: 24px; margin-top: 14px; }
  .meal-breakfast { top: 9px; }
  .meal-lunch { top: 221px; }
  .meal-dinner { top: 431px; }

  .speciality-title { position: absolute; left: 316px; top: 18px; color: var(--text-white); font-size: 25px; font-weight: 400; }
  .speciality-photo { position: absolute; left: 314px; top: 52px; width: 551px; height: 392px; background: radial-gradient(ellipse at 55% 55%, #f4f1ec 0%, #d9d4cc 45%, #4a4036 100%); }
  .side-photo { position: absolute; left: 865px; top: 52px; width: 335px; height: 120px; background: linear-gradient(90deg, #c9c6c0, #e9e6e1 60%, #b5b0a8); }
  .speciality-text { position: absolute; left: 316px; top: 450px; width: 876px; color: var(--text-white); font-size: 23px; line-height: 27px; }

  .site-footer { position: absolute; left: 0; top: 963px; width: 1200px; height: 46px; background: var(--footer-black); }
  .site-footer p { color: var(--text-white); font-size: 22px; line-height: 46px; margin-left: 27px; }
</style>
</head>
<body>
  <header class="site-header">
    <div class="sub-brand">
      <span class="sub-brand-mark"></span>
      <span class="sub-brand-name">Fernwick Table</span>
    </div>
    <div class="brand">
      <span class="brand-mark"></span>
      <span class="brand-name">Thistle Cafe</span>
    </div>
    <nav class="main-nav">
      <a href="#">About Us</a>
      <a href="#">Our Chefs</a>
      <a href="#">Menu</a>
      <a href="#">Drinks</a>
      <a href="#">Reservations</a>
      <a href="#">Contacts</a>
    </nav>
  </header>

  <main class="content-band">
    <aside class="meal-sidebar">
      <div class="meal meal-breakfast">
        <span class="meal-photo" role="img" aria-label="Plated breakfast dish with lemon and salad"></span>
        <p class="meal-label">Break Fast</p>
      </div>
      <div class="meal meal-lunch">
        <span class="meal-photo" role="img" aria-label="Plated lunch dish with lemon and salad"></span>
        <p class="meal-label">Lunch</p>
      </div>
      <div class="meal meal-dinner">
        <span class="meal-photo" role="img" aria-label="Plated dinner dish with lemon and salad"></span>
        <p class="meal-label">Dinner</p>
      </div>
    </aside>

    <h2 class="speciality-title">Today´s Speciality</h2>
    <div class="speciality-photo" role="img" aria-label="Crispy duck wrap on a white plate with a bowl of dark dipping sauce"></div>
    <div class="side-photo" role="img" aria-label="Second plated dish on a table"></div>
    <p class="speciality-text">Our cafe is not focus on a large A-la Carte menu. We serve our food according to the weather, the freshest ingredients and the likeness of our customers. We put eastern ideas into western cuisine. For example, we used crsioy boneless Peking Duck with seasoned fruit to make our wraps or using grilled teriyaki beef to serve our open sandwiches. We also set set menu in a reasonable price for our customers. We have 23 years of restaurant experience with passion in mastering our cuisine. We have a open kitchen and we use some raw materials such as brickwork and timber in our renovation. An open decking area for outdoor dining.</p>
  </main>

  <footer class="site-footer">
    <p>Copyrights Reserved 2011-2012</p>
  </footer>
</body>
</html>
```